Luxury Caviar Tin Label for High End Caviar Retailer

We are looking for a new caviar label design. We want something unique, preferably black and gold or dark blue and gold. We want a modern and luxurious feel. We have several types of caviar so we need to be able to change the name of the caviar when we print the labels. See inspiration attached. Logo is also attached. More about us: kvmarlune.com

Industry/Entity Type

fine foods industry, caviar

Font styles to use
Serif
Decorative

Requirements
Must have
• KV Marlune Logo, space for caviar name
Nice to have
• black and gold, blue and gold

```html
<!DOCTYPE html>
<html lang="en">
<head>
<meta charset="utf-8">
<title>KV Marlune Caviar Label</title>
<link rel="stylesheet" href="https://fonts.googleapis.com/css2?family=Cinzel:wght@700&family=Crimson+Text:wght@600&family=Marcellus&family=Roboto+Condensed:wght@700&display=swap">
<style>
  :root {
    --backdrop: #3b3b3d;
    --gold: #c4901c;
    --gold-rim: #d8b867;
    --navy: #0b0f52;
  }
  html, body {
    margin: 0;
    padding: 0;
    width: 1200px;
    height: 950px;
    overflow: hidden;
    background: var(--backdrop);
  }
  .label {
    display: block;
    width: 1200px;
    height: 950px;
  }
  .label-rim { fill: var(--gold-rim); }
  .label-border { fill: none; stroke: var(--navy); stroke-width: 7; }
  .label-field { fill: var(--navy); }
  .label-panel { fill: var(--gold); }
  .product-name {
    font-family: "Cinzel", serif;
    font-weight: 700;
    font-size: 74px;
    letter-spacing: 14px;
    fill: var(--navy);
  }
  .product-info {
    font-family: "Crimson Text", serif;
    font-weight: 600;
    font-size: 30px;
    fill: var(--navy);
  }
  .brand-name {
    font-family: "Marcellus", serif;
    font-size: 60px;
    fill: var(--navy);
  }
  .brand-web {
    font-family: "Roboto Condensed", sans-serif;
    font-weight: 700;
    font-size: 25px;
    letter-spacing: 2px;
    fill: var(--navy);
  }
</style>
</head>
<body>
<svg class="label" viewBox="0 0 1200 950" xmlns="http://www.w3.org/2000/svg" role="img" aria-label="KV Marlune caviar tin label">
  <defs>
    <clipPath id="label-face">
      <circle cx="600" cy="475" r="396"/>
    </clipPath>
  </defs>

  <circle class="label-rim" cx="600" cy="475" r="430"/>
  <circle class="label-panel" cx="600" cy="475" r="414"/>
  <circle class="label-border" cx="600" cy="475" r="403"/>

  <g clip-path="url(#label-face)">
    <rect class="label-field" x="200" y="75" width="800" height="800"/>
    <!-- top panel -->
    <rect class="label-panel" x="200" y="60" width="800" height="140"/>
    <rect class="label-panel" x="322" y="60" width="550" height="336" rx="30"/>
    <!-- bottom panel -->
    <rect class="label-panel" x="322" y="564" width="550" height="336" rx="30"/>
    <rect class="label-panel" x="200" y="755" width="800" height="140"/>
  </g>

  <text class="product-name" x="600" y="227" text-anchor="middle">CAVIAR</text>
  <text class="product-info" x="600" y="298" text-anchor="middle">Keep Refrigerated 28-34</text>
  <text class="product-info" x="600" y="346" text-anchor="middle">Ingredients: Caviar - Salt</text>

  <text class="brand-name" x="600" y="790" text-anchor="middle">KV MARLUNE</text>
  <text class="brand-web" x="600" y="835" text-anchor="middle">www.kvmarlune.com</text>
</svg>
</body>
</html>
```